Oil Field Service company needs professional business cards

Looking to clean up our current company business cards and look a little more professional. Harlow Casing Services is a US based company that services the oil field. We deal with engineers, managers and oil rigs....................................................................................................................................................................................................................................................................................................................................................................................................

Target Market(s)

Oil and Gas professionals

Industry/Entity Type

Oil And Gas

Contact Information for Business Card

See attached photo as example

Font styles to use
Sans Serif

Colors
ec1f27

Requirements
Must have
• Company Logo, Name, Title, Cell, Office, Fax, Email.
• See attached photo
Nice to have
• External CRT, Internal CRT, Casing Crews, Torque Turn, Laydown Machine
Should not have
• Do not introduce any new pictures and keep it professional looking

```html
<!DOCTYPE html>
<html lang="en">
<head>
<meta charset="UTF-8">
<title>Harlow Casing Services – Business Card</title>
<link href="https://fonts.googleapis.com/css2?family=Open+Sans:ital,wght@0,400;0,600;0,700;1,400&display=swap" rel="stylesheet">
<style>
  :root {
    --brand-red: #ec1f27;
    --slate: #46515b;
    --paper: #ffffff;
    --ink-grey: #5a636b;
    --backdrop: #e9e7e3;
  }
  html, body {
    margin: 0;
    padding: 0;
    width: 1200px;
    height: 950px;
    overflow: hidden;
    background: var(--backdrop);
    font-family: "Open Sans", Arial, sans-serif;
  }
  .sheet {
    position: relative;
    width: 1200px;
    height: 950px;
  }
  .card {
    position: absolute;
    left: 250px;
    width: 700px;
    height: 400px;
    overflow: hidden;
    box-shadow: 0 6px 18px rgba(0,0,0,0.18);
  }
  .card--front { top: 55px; background: var(--paper); }
  .card--back { top: 495px; background: var(--brand-red); color: var(--paper); }

  .card__panel { position: absolute; inset: 0; }

  .brand {
    position: absolute;
    font-weight: 700;
    text-transform: uppercase;
    line-height: 1.05;
    margin: 0;
  }
  .brand__main { display: block; font-size: 54px; letter-spacing: 2px; }
  .brand__sub { display: block; font-size: 17px; letter-spacing: 4px; margin-top: 6px; }

  .card--front .brand { left: 50px; top: 150px; color: var(--ink-grey); }

  .contact {
    position: absolute;
    right: 34px;
    top: 34px;
    width: 300px;
    text-align: right;
    color: var(--paper);
  }
  .contact__name { font-size: 25px; font-weight: 600; margin: 0; }
  .contact__title { font-size: 15px; margin: 2px 0 26px; }
  .contact__line {
    font-size: 15px;
    margin: 0 0 7px;
    display: flex;
    justify-content: flex-end;
    align-items: center;
    gap: 10px;
  }
  .contact__icon { width: 14px; height: 14px; flex: none; }
  .contact__web { font-size: 15px; letter-spacing: 2px; margin-top: 12px; }

  .card--back .brand { left: 150px; top: 95px; color: var(--paper); }
  .services {
    position: absolute;
    left: 150px;
    top: 250px;
    margin: 0;
    font-size: 19px;
    font-style: italic;
    line-height: 1.45;
  }
</style>
</head>
<body>
<main class="sheet">

  <section class="card card--front" aria-label="Card front">
    <svg class="card__panel" viewBox="0 0 700 400" width="700" height="400" aria-hidden="true">
      <path d="M300 0 H700 V400 H430 C 385 300, 330 160, 300 0 Z" fill="var(--slate)"/>
      <path d="M300 0 C 330 160, 385 300, 430 400" fill="none" stroke="var(--brand-red)" stroke-width="7"/>
    </svg>

    <h1 class="brand">
      <span class="brand__main">Harlow</span>
      <span class="brand__sub">Casing Services</span>
    </h1>

    <div class="contact">
      <p class="contact__name">Cody Brannan</p>
      <p class="contact__title">Area Manager</p>
      <p class="contact__line">Fairview, OK 73700</p>
      <p class="contact__line">(555)210-4400
        <svg class="contact__icon" viewBox="0 0 14 14"><path d="M3 1 L5 1 L6 4 L4.5 5.5 Q6 8.5 8.5 9.5 L10 8 L13 9 L13 11 Q13 13 11 13 Q1 12 1 3 Q1 1 3 1 Z" fill="var(--paper)"/></svg>
      </p>
      <p class="contact__line">(555)318-2275
        <svg class="contact__icon" viewBox="0 0 14 14"><rect x="3.5" y="1" width="7" height="12" rx="1.2" fill="none" stroke="var(--paper)" stroke-width="1.4"/><circle cx="7" cy="11" r="0.8" fill="var(--paper)"/></svg>
      </p>
      <p class="contact__line">(555)210-4411
        <svg class="contact__icon" viewBox="0 0 14 14"><rect x="3" y="1" width="8" height="5" fill="none" stroke="var(--paper)" stroke-width="1.3"/><rect x="1" y="6" width="12" height="7" rx="1" fill="var(--paper)"/></svg>
      </p>
      <p class="contact__line">cody@harlowcasing.com
        <svg class="contact__icon" viewBox="0 0 14 14"><rect x="1" y="3" width="12" height="8" fill="var(--paper)"/><path d="M1 3 L7 8 L13 3" fill="none" stroke="var(--slate)" stroke-width="1.2"/></svg>
      </p>
      <p class="contact__web">www.harlowcasing.com</p>
    </div>
  </section>

  <section class="card card--back" aria-label="Card back">
    <h2 class="brand">
      <span class="brand__main">Harlow</span>
      <span class="brand__sub">Casing Services</span>
    </h2>
    <p class="services">External CRT | Internal CRT | Casing Crews<br>Torque Turn | Laydown Machine</p>
  </section>

</main>
</body>
</html>
```